Bref créative
Corporate Advisory
Professional
Dorian Pelhame
Director
Level 3, 412 Brindle Street, Kelvin Grove. QLD 4059
dorian.pelhame@veltrina.com.au
www.veltrina.com.au
Corporate colours are the blue and white in logo. Front may be one colour eg white with blue logo and rear may be blue with white logo
Can be as simple as blue background and white logo
Veltrina logo - white background with blue logo is primary and blue background with white logo is secondary - no other coloures used.

```html
<!DOCTYPE html>
<html lang="en">
<head>
<meta charset="utf-8">
<title>Veltrina Stationery</title>
<link rel="stylesheet" href="https://fonts.googleapis.com/css2?family=Raleway:wght@300;400;600&display=swap">
<style>
  :root {
    --navy: #1f3a57;
    --white: #ffffff;
    --backdrop: #e6e7e9;
    --ink-soft: #5b6c7e;
  }
  * { margin: 0; padding: 0; box-sizing: border-box; }
  html, body { width: 1200px; height: 1000px; overflow: hidden; }
  body {
    background: var(--backdrop);
    font-family: "Raleway", Arial, sans-serif;
    color: var(--navy);
    position: relative;
  }
  .sheet { position: absolute; box-shadow: 0 3px 10px rgba(0,0,0,0.22); }

  /* Business card front */
  .card-front {
    left: 22px; top: 135px; width: 248px; height: 149px;
    background: var(--white); padding: 16px 16px;
  }
  .card-front .person { font-size: 11px; font-weight: 600; letter-spacing: 0.5px; text-transform: uppercase; }
  .card-front .role { font-size: 8px; color: var(--ink-soft); margin-bottom: 9px; }
  .card-front .contact { font-size: 7px; line-height: 1.45; color: var(--ink-soft); }
  .card-front .brand { position: absolute; left: 16px; bottom: 14px; }

  /* Business card back */
  .card-back {
    left: 292px; top: 135px; width: 248px; height: 149px;
    background: var(--navy); color: var(--white);
  }
  .card-back .brand { position: absolute; left: 34px; top: 52px; }
  .card-back .brand .wordmark { color: var(--white); font-size: 22px; }
  .card-back .brand .mark-square { background: var(--white); width: 30px; height: 30px; }
  .card-back .web { position: absolute; right: 14px; bottom: 14px; font-size: 7px; letter-spacing: 0.3px; }

  /* Brand lockup */
  .brand { display: flex; align-items: center; gap: 8px; }
  .mark-square { width: 18px; height: 18px; background: var(--navy); flex: none; }
  .wordmark { font-weight: 300; font-size: 18px; letter-spacing: 2px; text-transform: uppercase; color: var(--navy); line-height: 1; }
  .tagline { font-size: 7px; letter-spacing: 1px; text-transform: uppercase; color: var(--navy); margin-top: 4px; white-space: nowrap; }

  /* Letterhead */
  .letterhead {
    left: 567px; top: 162px; width: 608px; height: 798px;
    background: var(--white);
  }
  .letterhead .side-band {
    position: absolute; top: 0; right: 0; bottom: 0; width: 24px; background: var(--navy);
  }
  .vertical-details {
    position: absolute; color: var(--white); font-size: 7px; letter-spacing: 0.4px;
    writing-mode: vertical-rl; transform: rotate(180deg); white-space: nowrap;
  }
  .letterhead .vertical-details { right: 7px; bottom: 100px; }
  .letterhead .brand-block { position: absolute; left: 32px; bottom: 28px; }
  .letterhead .wordmark { font-size: 52px; letter-spacing: 5px; }
  .letterhead .mark-square { width: 48px; height: 48px; }
  .letterhead .tagline { font-size: 12px; letter-spacing: 2px; margin-left: 58px; }

  /* Envelope */
  .envelope {
    left: 22px; top: 513px; width: 675px; height: 297px;
    background: var(--white); overflow: hidden;
  }
  .envelope .flap { position: absolute; left: 0; top: 0; }
  .envelope .return-line {
    position: absolute; left: 0; right: 20px; top: 40px; text-align: center;
    color: var(--white); font-size: 6px; letter-spacing: 0.3px;
  }
  .envelope .side-band { position: absolute; top: 0; right: 0; bottom: 0; width: 20px; background: var(--navy); }
  .envelope .vertical-details { right: 6px; bottom: 20px; font-size: 6px; }
  .envelope .brand-block { position: absolute; left: 395px; bottom: 26px; }
  .envelope .wordmark { font-size: 36px; letter-spacing: 3px; }
  .envelope .mark-square { width: 34px; height: 34px; }
  .envelope .tagline { font-size: 8px; margin-left: 42px; }
</style>
</head>
<body>

  <section class="sheet card-front" aria-label="Business card front">
    <p class="person">Dorian Pelhame</p>
    <p class="role">Director</p>
    <p class="contact">
      Level 3, 412 Brindle Street, Kelvin Grove. QLD 4059<br>
      Phone: +61 7 3555 0142<br>
      Mobile: 0400 555 018<br>
      Fax: +61 7 3555 0143<br>
      Email: dorian.pelhame@veltrina.com.au
    </p>
    <div class="brand">
      <span class="mark-square"></span>
      <span class="wordmark">Veltrina</span>
    </div>
  </section>

  <section class="sheet card-back" aria-label="Business card back">
    <div class="brand">
      <span class="mark-square"></span>
      <span class="wordmark">Veltrina</span>
    </div>
    <p class="web">www.veltrina.com.au</p>
  </section>

  <section class="sheet letterhead" aria-label="Letterhead">
    <div class="side-band">
      <p class="vertical-details">Level 3, 412 Brindle Street, Kelvin Grove. QLD 4059 &nbsp;&nbsp; P: +61 7 3555 0142 &nbsp;&nbsp; F: +61 7 3555 0143 &nbsp;&nbsp; www.veltrina.com.au</p>
    </div>
    <div class="brand-block">
      <div class="brand">
        <span class="mark-square"></span>
        <span class="wordmark">Veltrina</span>
      </div>
      <p class="tagline">Trusted advice, clearly delivered</p>
    </div>
  </section>

  <section class="sheet envelope" aria-label="Envelope">
    <svg class="flap" width="675" height="110" viewBox="0 0 675 110">
      <polygon points="0,0 675,0 675,42 337,100 0,42" fill="var(--navy)"/>
    </svg>
    <p class="return-line">Level 3, 412 Brindle Street, Kelvin Grove</p>
    <div class="side-band">
      <p class="vertical-details">Level 3, 412 Brindle Street, Kelvin Grove. QLD 4059</p>
    </div>
    <div class="brand-block">
      <div class="brand">
        <span class="mark-square"></span>
        <span class="wordmark">Veltrina</span>
      </div>
      <p class="tagline">Trusted advice, clearly delivered</p>
    </div>
  </section>

</body>
</html>
```